Corvella Foundation is a new grant making charity set up in the UK.

Having got a logo, we now need a website to go with it. We have worked out the text which people are going to need in order to then apply for grants. But having found out what we require they will probably need to go away and think about it.
We have to be careful of what images we use. So I have uploaded some images that we like. We are also going to be adding more pages almost immediately so need to think about the images for these.
I know basic wordpress so I will be able to add new pages/make alterations in future.
Updates
The website does need to be coded in Wordpress so that I can maintain it afterwards.
Marisse
Brief changed to provide more money and we have also provided more possible pictures. And generally more explanation.
Target Market(s)
departments in universities, other charities doing work on relief of pain, people working in health service departments
Industry/Entity Type
Health Charity
Coding
Coded - Design and coding required
Number of Pages Required
4 page
Look and feel
Each slider illustrates characteristics of the customer's brand and the style your logo design should communicate.

```html
<!DOCTYPE html>
<html lang="en">
<head>
<meta charset="utf-8">
<title>Corvella Foundation</title>
<link rel="stylesheet" href="https://fonts.googleapis.com/css2?family=Mulish:wght@400;600;700;800&family=Raleway:wght@400;500&family=Roboto+Condensed:wght@400&display=swap">
<style>
:root{
  --brand:#0b6cb8;
  --brand-bright:#2f95e6;
  --footer:#0a71c2;
  --ink:#333a44;
  --white:#ffffff;
  --ghost:#f1f2f4;
}
*{margin:0;padding:0;box-sizing:border-box}
html,body{width:748px;height:1200px;overflow:hidden;background:var(--white)}
body{position:relative;font-family:'Mulish',sans-serif;color:var(--ink)}
.abs{position:absolute}

/* Hero */
.hero{left:0;top:0;width:748px;height:298px;
  background:radial-gradient(circle at 22% 42%,rgba(214,150,60,.45),transparent 14%),
             radial-gradient(circle at 80% 48%,rgba(214,150,60,.45),transparent 16%),
             radial-gradient(circle at 40% 22%,#2c4a78,transparent 40%),
             linear-gradient(160deg,#13233f,#1b2f52 50%,#0f1c33)}
.brand{left:94px;top:14px;display:flex;align-items:center;gap:6px;color:var(--white);
  font-family:'Mulish',sans-serif;font-weight:700;font-size:14px;letter-spacing:.5px}
.brand-mark{width:22px;height:22px;border:2px solid var(--white)}
.nav{right:94px;top:18px;display:flex;font-family:'Raleway',sans-serif;font-size:8.5px}
.nav a{color:var(--white);text-decoration:none;padding:0 14px;border-left:1px solid rgba(255,255,255,.3);line-height:12px}
.nav a:first-child{border-left:0;color:var(--brand-bright)}
.nav a:last-child{padding-right:0}
.hero-title{left:0;top:132px;width:748px;text-align:center;color:var(--white);
  font-family:'Roboto Condensed',sans-serif;font-size:24.5px;line-height:35px}

/* Framed photos */
.frame{border:1px solid var(--brand);padding:3px;width:245px;height:244px}
.photo{width:100%;height:100%}
.photo-pain{background:radial-gradient(circle at 80% 35%,#f6c7d8,transparent 10%),
  radial-gradient(ellipse at 52% 55%,#e0641e,#a8321a 30%,transparent 55%),
  linear-gradient(180deg,#4a4a4a,#151515)}
.photo-pills{background:radial-gradient(ellipse at 45% 60%,#8fc96a,transparent 22%),
  radial-gradient(ellipse at 72% 75%,#6aa5e0,transparent 22%),
  linear-gradient(135deg,#f2b33a,#e58a2a 40%,#dce9f5 65%,#3d7ec9)}

.section-title{color:var(--brand);font-weight:700;font-size:17px}
.copy{font-size:10.5px;line-height:19px;font-weight:600}
.reg-line{display:flex;align-items:center;gap:7px;color:var(--brand);font-size:11.5px;font-weight:600}

/* Mission */
.ghost-word{left:214px;top:604px;font-family:'Mulish',sans-serif;font-weight:800;font-size:76px;
  letter-spacing:3px;color:var(--ghost)}
.mission-title{left:130px;top:637px;color:var(--brand);font-weight:800;font-size:21px}
.mission-copy{left:297px;top:617px;width:340px;font-size:11.5px;line-height:20.3px;font-weight:600}

.text-link{color:var(--brand);font-size:11.5px;font-weight:600;text-decoration:none;border-bottom:1px solid var(--brand);padding-bottom:1px}

/* Footer */
.footer{left:0;top:1011px;width:748px;height:189px;background:var(--footer);color:var(--white)}
.footer-brand{left:0;top:36px;width:748px;display:flex;justify-content:center;align-items:center;gap:8px;
  font-weight:700;font-size:22px;letter-spacing:1px;color:#cfe3f6}
.footer-brand .brand-mark{width:30px;height:30px;border-color:#cfe3f6}
.contact{display:flex;align-items:center;gap:8px;font-family:'Raleway',sans-serif;font-size:8.5px;line-height:14px}
.icon-box{width:30px;height:30px;border:1px solid rgba(255,255,255,.35);display:flex;align-items:center;justify-content:center}
.rule{left:100px;top:153px;width:547px;height:1px;background:rgba(255,255,255,.3)}
.copyright{left:103px;top:165px;font-family:'Raleway',sans-serif;font-size:8px}
.socials{left:549px;top:162px;display:flex;gap:7px}
.socials span{width:19px;height:19px;border:1px solid var(--white);border-radius:50%}
</style>
</head>
<body>

<header class="abs hero" role="img" aria-label="Close-up illustration of glowing nerve cells on a dark blue background">
</header>
<div class="abs brand"><span class="brand-mark"></span>Corvella Foundation</div>
<nav class="abs nav"><a href="#">Home</a><a href="#">About Us</a><a href="#">Grants</a><a href="#">Contact Us</a></nav>
<h1 class="abs hero-title">We Get Funding ForPain Research or Education,<br>To Help Prevent People Who Are Suffering Chronic Pain</h1>

<section>
  <div class="abs frame" style="left:94px;top:336px">
    <div class="photo photo-pain" role="img" aria-label="Illustration of a seated figure with a glowing orange skeleton showing pain"></div>
  </div>
  <h2 class="abs section-title" style="left:374px;top:390px">About Corvella Foundation</h2>
  <p class="abs copy" style="left:374px;top:419px;width:290px">Corvella Foundation is a grant making charity set up in the UK in 2021.</p>
  <p class="abs copy" style="left:374px;top:461px;width:290px">The main aim of Corvella Foundation is to reduce the suffering caused by chronic pain.</p>
  <div class="abs reg-line" style="left:374px;top:510px">
    <svg width="17" height="17" viewBox="0 0 17 17" fill="none" stroke="currentColor" stroke-width="1"><rect x="1.5" y="2.5" width="10" height="13"/><path d="M4 1.5h5v2H4z"/><path d="M3.5 7h6M3.5 9.5h6M3.5 12h3"/><path d="M15.5 8.5l-5 6-2 .7.6-2 5-6z"/></svg>
    Charity Registration Number 1187305
  </div>
</section>

<section>
  <div class="abs ghost-word" aria-hidden="true">MISSION</div>
  <h2 class="abs mission-title">Our Mission</h2>
  <svg class="abs" style="left:270px;top:630px" width="8" height="36" viewBox="0 0 8 36"><line x1="2" y1="10" x2="2" y2="26" stroke="#0b6cb8"/><line x1="5.5" y1="0" x2="5.5" y2="36" stroke="#0b6cb8"/></svg>
  <p class="abs mission-copy">Lorem ipsum dolor sit amet, consectetuer adipiscing elit, sed diam nonummy nibh euismod tincidunt ut laoreet dolore magna aliquam erat volutpat.</p>
</section>

<section>
  <h2 class="abs section-title" style="left:94px;top:769px">Lorem Ipsum Dolor Sit Amet</h2>
  <p class="abs copy" style="left:94px;top:796px;width:285px;line-height:18.6px">Lorem ipsum dolor sit amet, consectetuer adipiscing elit, sed diam nonummy nibh euismod tincidunt ut laoreet dolore magna aliquloorem ipsum dolor sit amet, consectetuer adipiscing elit, sed diam nonummy nibh euismod tincidunt.</p>
  <a class="abs text-link" href="#" style="left:95px;top:893px">Contact Me Today</a>
  <div class="abs frame" style="left:409px;top:720px">
    <div class="photo photo-pills" role="img" aria-label="Photo of pill bottles spilling colourful tablets"></div>
  </div>
</section>

<footer class="abs footer">
  <div class="abs footer-brand"><span class="brand-mark"></span>CORVELLA FOUNDATION</div>
  <div class="abs contact" style="left:100px;top:100px">
    <span class="icon-box"><svg width="14" height="14" viewBox="0 0 14 14" fill="none" stroke="#fff" stroke-width=".9"><path d="M1.5 6v7h11V6L7 2z"/><path d="M1.5 6L7 10l5.5-4"/><path d="M3.5 5.5V3.5h7v2"/></svg></span>
    <div>Email<br>info@corvellafoundation.com</div>
  </div>
  <div class="abs contact" style="left:348px;top:100px">
    <span class="icon-box"><svg width="14" height="14" viewBox="0 0 14 14" fill="none" stroke="#fff" stroke-width=".9"><path d="M3 1.5l2 3-1.2 1.2c.8 1.7 2 2.9 3.6 3.6L8.6 8l3 2-1.2 2.3C6 12 2 8 1.7 3z"/><path d="M8.5 1.5a4 4 0 014 4M8.5 3.5a2 2 0 012 2"/></svg></span>
    <div>Phone<br>123-456-7890</div>
  </div>
  <div class="abs contact" style="left:527px;top:100px">
    <span class="icon-box"><svg width="15" height="15" viewBox="0 0 17 17" fill="none" stroke="#fff" stroke-width="1"><rect x="1.5" y="2.5" width="10" height="13"/><path d="M4 1.5h5v2H4z"/><path d="M3.5 7h6M3.5 9.5h6M3.5 12h3"/><path d="M15.5 8.5l-5 6-2 .7.6-2 5-6z"/></svg></span>
    <div>Charity Registration<br>1187305</div>
  </div>
  <div class="abs rule"></div>
  <p class="abs copyright">Copyright © 2021 Corvella Foundation. All Rights Reserved.</p>
  <div class="abs socials" aria-label="Social links"><span></span><span></span><span></span><span></span></div>
</footer>

</body>
</html>
```